Keystone BRISK Repairs Business card

Keystone Motors is looking for a business card design for our detailing wing "Keystone BRISK Repairs"
The services offered are vehicle paintless dent repairs, vehicle detailing, scratch and bumper repairs & paint and alloy wheel repairs.
Ideally the card design should be sharp, neat and professional. We are not looking for a card with pictures of cars.
Our corporate colours are blues (as in the logo supplied) which may look good with water droplets in high res and perhaps one or two images leaking off the card. Dark blacks with electric blues perhaps.
Images may be of a spray gun (we use Torvanex), a rotary polisher (Quill WideStep) or similar objects used in the processes.

Industry/Entity Type

Paint

Contact Information for Business Card

Title: Keystone BRISK Repairs
Services: Bumper Repairs
Scratch/Paint Repairs
Paintless dent repairs
Alloy wheel repairs
Name: Martin K
Telephone: 0427195364
Email : martin@keystonemotors.com.au

Font styles to use
Sans Serif
Other font styles liked:

Colors
0355a3
3277b5
0792cd
cfdfed

Requirements
Must have
• The title - "Keystone BRISK Repairs" should be a focus on either the from or back of the card
Should not have
• Photographs of cars

```html
<!DOCTYPE html>
<html lang="en">
<head>
<meta charset="utf-8">
<title>Keystone BRISK Repairs – Business Card</title>
<link rel="stylesheet" href="https://fonts.googleapis.com/css2?family=Open+Sans:wght@400;600;700&family=Roboto+Condensed:wght@700&display=swap">
<style>
  :root {
    --stage: #e6e7e9;
    --card-black: #0b0b0c;
    --silver: #c6c9cd;
    --navy: #0a1f5c;
    --royal: #0355a3;
    --mid-blue: #3277b5;
    --electric: #0792cd;
    --ice: #cfdfed;
    --ink: #1b2a4a;
    --white: #ffffff;
  }
  * { box-sizing: border-box; margin: 0; padding: 0; }
  html, body { width: 1200px; height: 768px; overflow: hidden; }
  body {
    background: var(--stage);
    font-family: "Open Sans", Arial, sans-serif;
    position: relative;
  }
  .card {
    position: absolute;
    top: 229px;
    width: 540px;
    height: 310px;
    border-radius: 4px;
    overflow: hidden;
    box-shadow: 0 6px 18px rgba(0,0,0,.18);
  }
  /* Front */
  .card--front { left: 40px; background: var(--card-black); }
  .front-brand {
    position: absolute; inset: 0;
    display: flex; align-items: center; justify-content: center; gap: 16px;
  }
  .brand-dot {
    width: 44px; height: 44px; border-radius: 50%;
    background: var(--silver);
  }
  .front-brand .brand-name {
    font-weight: 700; font-size: 32px; letter-spacing: 1px;
    color: var(--silver); text-transform: uppercase;
  }
  /* Back */
  .card--back { left: 620px; background: var(--white); }
  .waves { position: absolute; inset: 0; }
  .back-brand {
    position: absolute; left: 28px; top: 30px;
    display: flex; align-items: center; gap: 10px;
  }
  .back-brand .brand-dot { width: 30px; height: 30px; background: var(--navy); }
  .back-brand .brand-name {
    font-weight: 700; font-size: 22px; color: var(--navy);
    text-transform: uppercase; letter-spacing: .5px;
  }
  .holder { position: absolute; left: 30px; top: 86px; color: var(--ink); }
  .holder-name { font-weight: 700; font-size: 14px; }
  .holder-role { font-size: 9.5px; margin-top: 1px; }
  .contacts { list-style: none; margin-top: 8px; }
  .contacts li {
    display: flex; align-items: center; gap: 8px;
    font-size: 12px; line-height: 19px; color: var(--ink);
  }
  .contacts svg { width: 10px; height: 10px; fill: var(--mid-blue); flex: none; }
  .title {
    position: absolute; right: 22px; top: 84px;
    font-family: "Roboto Condensed", "Arial Narrow", sans-serif;
    font-weight: 700; font-size: 23px; color: var(--royal);
  }
  .services {
    position: absolute; right: 22px; bottom: 10px;
    text-align: right; color: var(--white);
  }
  .services h2 { font-size: 14px; font-weight: 700; line-height: 18px; margin-bottom: 1px; }
  .services ul { list-style: none; }
  .services li { font-size: 13px; line-height: 18px; }
</style>
</head>
<body>

<section class="card card--front" aria-label="Card front">
  <div class="front-brand">
    <span class="brand-dot"></span>
    <span class="brand-name">Keystone Motors</span>
  </div>
</section>

<section class="card card--back" aria-label="Card back">
  <svg class="waves" viewBox="0 0 540 310" aria-hidden="true">
    <path d="M0,206 C110,226 220,232 320,214 C410,196 480,160 540,126" fill="none" stroke="var(--ice)" stroke-width="7"/>
    <path d="M0,214 C110,234 220,240 320,222 C410,204 480,168 540,134" fill="none" stroke="var(--electric)" stroke-width="7"/>
    <path d="M0,224 C110,244 220,250 320,232 C410,214 480,178 540,144" fill="none" stroke="var(--mid-blue)" stroke-width="4"/>
    <path d="M0,232 C110,252 220,258 320,240 C410,222 480,186 540,150 L540,310 L0,310 Z" fill="var(--navy)"/>
  </svg>

  <div class="back-brand">
    <span class="brand-dot"></span>
    <span class="brand-name">Keystone Motors</span>
  </div>

  <div class="holder">
    <p class="holder-name">Martin K</p>
    <p class="holder-role">Managing Director</p>
    <ul class="contacts">
      <li><svg viewBox="0 0 10 10"><path d="M2 0h2l1 2.5-1.3 1a6 6 0 0 0 2.8 2.8l1-1.3L10 6v2a2 2 0 0 1-2 2A8 8 0 0 1 0 2a2 2 0 0 1 2-2z"/></svg>0427195364</li>
      <li><svg viewBox="0 0 10 10"><path d="M0 1.5h10v7H0z M0.6 2.2L5 5.6 9.4 2.2" stroke="#fff" stroke-width=".8"/></svg>martin@keystonemotors.com.au</li>
      <li><svg viewBox="0 0 10 10"><circle cx="5" cy="5" r="5"/></svg>www.keystonemotors.com.au</li>
    </ul>
  </div>

  <h1 class="title">Keystone BRISK Repairs</h1>

  <div class="services">
    <h2>Our Services:</h2>
    <ul>
      <li>Bumper Repairs «</li>
      <li>Alloy wheel Repairs «</li>
      <li>Scratch/Paint Repairs «</li>
      <li>Paintless dent Repairs «</li>
    </ul>
  </div>
</section>

</body>
</html>
```